Property Finance Company - Orin Ventures Limited

Background: Orin Ventures Group Limited is a private property finance company. Orin Ventures Group has capital to directly fund first mortgage, mezzanine and preferred equity financing. We also acquire performing, sub-performing and distressed debt.

Orin Ventures' management philosophy emphasises expertise, innovation, wisdom, honesty and competitiveness. Orin Ventures are not finance brokers - we provide debt funding to the commercial property and residential development sectors. Our process is built from experience and cumutavely Orin Ventures' Directors have in excess of 60 years wisdom.

The aim of the website will be to increase brand awareness, provide clients with comfort around our level of skill and background on who we are, generate more sales, and provide examples of projects that we have funded.

The website is a new product launch, and we need to use our Orin Ventures logo that has just been designed. We like a dark background, and either black/silver/grey/ jade green, or black/gold/jade green colours.

Our unique advantages are that we have fast turnaround times, we can solve clients funding problems and we know what we are doing. Our target audience will be viewing the website on both desktop and mobile devices.

We would like to have the following pages:

Home
About
Team
Services
Project Experience
Contact

Competitors Website: http://www.tarvelo.com/

We would also like to have the option of video footage in our website, as you can see in our competitors website.

Overall we want a really slick, elegant but modern website that is better than www.tarvelo.com

Target Market(s)

Finance borrowers, property developers, accountants, lawyers, businesspeople, high net worth people

Industry/Entity Type

Finance

Requirements
Must have
• Please see project description
Nice to have
Should not have

```html
<!DOCTYPE html>
<html lang="en">
<head>
<meta charset="utf-8">
<title>Orin Ventures Group</title>
<link rel="stylesheet" href="https://fonts.googleapis.com/css2?family=Open+Sans:wght@400;600&family=Roboto:wght@400;500&display=swap">
<style>
:root{
  --ink:#ffffff;
  --muted:#d2d2d2;
  --about-bg:#2f2f2f;
  --jade-dark:#02140a;
  --jade:#0f8a45;
  --projects-bg:#171717;
  --contact-bg:#2b2b2b;
  --footer-bg:#232323;
  --line:#ffffff;
}
*{margin:0;padding:0;box-sizing:border-box}
html,body{width:1200px;height:2715px;overflow:hidden;background:#000}
body{font-family:"Open Sans",sans-serif;color:var(--ink);position:relative}
.heading{font-family:"Roboto",sans-serif;font-weight:400;letter-spacing:.5px}
section,header,footer{position:absolute;left:0;width:1200px}
.btn{position:absolute;display:flex;align-items:center;justify-content:center;border:2px solid var(--line);font-family:"Roboto",sans-serif;font-size:14px;letter-spacing:.5px;color:var(--ink)}

/* hero */
.hero{top:0;height:673px;background:#1c1d20}
.hero-photo{position:absolute;inset:0;background:
  radial-gradient(ellipse 700px 260px at 50% 0%,rgba(176,132,58,.75),rgba(120,92,48,0) 70%),
  radial-gradient(ellipse 420px 520px at 1000px 380px,rgba(8,9,11,.85),rgba(8,9,11,0) 75%),
  radial-gradient(ellipse 380px 220px at 80px 520px,rgba(90,86,78,.55),rgba(90,86,78,0) 75%),
  linear-gradient(180deg,#6b5630 0%,#4a4134 18%,#33322f 40%,#26282b 65%,#1a1b1e 100%)}
.brand{position:absolute;left:120px;top:30px;display:flex;align-items:center;gap:14px}
.brand-mark{width:86px;height:86px;border-radius:50%;background:rgba(255,255,255,.92)}
.brand-name{font-family:"Roboto",sans-serif;font-weight:400;font-size:25px;letter-spacing:1px;line-height:1.15;text-align:center}
.main-nav{position:absolute;left:490px;top:60px;display:flex;gap:29px;font-family:"Roboto",sans-serif;font-size:15px;text-transform:uppercase}
.main-nav .active{position:relative}
.main-nav .active::after{content:"";position:absolute;left:0;right:0;top:24px;height:2px;background:var(--ink)}
.play{position:absolute;left:536px;top:277px}
.scroll-cue{position:absolute;left:582px;top:630px}

/* about */
.about{top:673px;height:395px;background:var(--about-bg);text-align:center}
.about .eyebrow{position:absolute;top:52px;width:100%;font-size:20px;color:var(--muted)}
.about h1{position:absolute;top:82px;width:100%;font-size:28px}
.about p{position:absolute;top:140px;left:185px;width:830px;font-size:13px;line-height:28px;color:var(--muted)}
.about .btn{left:530px;top:256px;width:154px;height:39px}

/* services */
.services{top:1068px;height:430px;background:linear-gradient(110deg,var(--jade-dark) 0%,#06331b 45%,var(--jade) 100%)}
.services h2{position:absolute;top:36px;width:100%;text-align:center;font-size:27px}
.service{position:absolute;top:108px;width:300px;text-align:center}
.service-icon{width:104px;height:104px;border-radius:50%;background:rgba(24,130,70,.4);margin:0 auto}
.service h3{margin-top:26px;font-size:17px;font-weight:500;text-transform:uppercase}
.service p{margin:10px auto 0;width:260px;font-size:10.5px;line-height:18px;color:#e4e4e4}
.service .more{margin-top:12px;font-family:"Roboto",sans-serif;font-size:14px}

/* projects */
.projects{top:1498px;height:557px;background:var(--projects-bg)}
.projects h2{position:absolute;top:42px;width:100%;text-align:center;font-size:27px}
.tile{position:absolute}
.tile-a{left:157px;top:107px;width:283px;height:178px;background:
  linear-gradient(90deg,rgba(70,70,70,.85) 0%,rgba(70,70,70,.6) 55%,rgba(40,40,40,.2) 100%),
  linear-gradient(160deg,#5c6268 0%,#2d3034 60%,#1c1d20 100%)}
.tile-a h3{position:absolute;left:42px;top:57px;font-size:17px;font-weight:500}
.tile-a p{position:absolute;left:42px;top:84px;width:200px;font-size:10.5px;line-height:16px;color:#e2e2e2}
.tile-b{left:157px;top:297px;width:283px;height:175px;background:
  radial-gradient(ellipse 160px 110px at 30% 80%,rgba(226,234,242,.9),rgba(226,234,242,0) 80%),
  linear-gradient(135deg,#4b5763 0%,#9fb4c8 40%,#cfd9e3 65%,#5d6a5a 100%)}
.tile-c{left:451px;top:107px;width:598px;height:365px;background:
  radial-gradient(ellipse 240px 170px at 8% 88%,rgba(255,232,120,.95),rgba(240,190,60,0) 75%),
  radial-gradient(ellipse 230px 260px at 78% 55%,rgba(196,160,96,.75),rgba(160,120,70,0) 80%),
  radial-gradient(ellipse 200px 90px at 25% 12%,rgba(245,248,252,.8),rgba(245,248,252,0) 80%),
  linear-gradient(180deg,#3f7fb8 0%,#7fa9cf 35%,#b9944e 70%,#3c3a20 100%)}
.projects .btn{left:525px;top:497px;width:173px;height:38px;font-size:12px}

/* experience */
.experience{top:2055px;height:430px;background:linear-gradient(120deg,#9a9a9a 0%,#7d7d7d 45%,#5a5a5a 100%)}
.experience .building{position:absolute;left:0;top:30px;width:630px;height:400px;background:
  linear-gradient(150deg,#f2f2f2 0%,#bdbdbd 40%,#6e6e6e 75%,#3a3a3a 100%);
  clip-path:polygon(0 15%,35% 0,100% 100%,0 100%)}
.experience h2{position:absolute;left:582px;top:84px;font-size:27px}
.experience p{position:absolute;left:582px;top:140px;width:470px;font-size:13.5px;line-height:28px;color:#ececec}
.experience .btn{left:587px;top:281px;width:153px;height:38px}

/* contact strip */
.contact{top:2485px;height:92px;background:var(--contact-bg);font-family:"Roboto",sans-serif;font-size:15px}
.contact-item{position:absolute;top:35px;display:flex;align-items:center;gap:10px}

/* footer */
.site-footer{top:2577px;height:138px;background:var(--footer-bg)}
.footer-nav{position:absolute;left:146px;top:36px;display:flex;gap:24px;font-family:"Roboto",sans-serif;font-size:13px;text-transform:uppercase}
.copyright{position:absolute;left:150px;top:70px;font-size:12px;color:#bdbdbd}
.social{position:absolute;left:914px;top:31px;display:flex;gap:7px}
.social span{width:34px;height:34px;border:2px solid var(--line);border-radius:50%}
</style>
</head>
<body>

<header class="hero">
  <div class="hero-photo" role="img" aria-label="Dusk city skyline with high-rise towers beside a river"></div>
  <div class="brand">
    <span class="brand-mark"></span>
    <span class="brand-name">ORIN VENTURES<br>GROUP</span>
  </div>
  <nav class="main-nav">
    <span class="active">Home</span><span>About</span><span>Team</span><span>Services</span><span>Project Experience</span><span>Contact</span>
  </nav>
  <svg class="play" width="128" height="128" viewBox="0 0 128 128" aria-label="Play video">
    <circle cx="64" cy="64" r="60" fill="none" stroke="#fff" stroke-width="4"/>
    <path d="M52 40 L86 64 L52 88 Z" fill="none" stroke="#fff" stroke-width="4" stroke-linejoin="round"/>
  </svg>
  <svg class="scroll-cue" width="36" height="20" viewBox="0 0 36 20" aria-hidden="true">
    <path d="M2 2 L18 17 L34 2" fill="none" stroke="#fff" stroke-width="2"/>
  </svg>
</header>

<section class="about">
  <div class="eyebrow heading">— ABOUT —</div>
  <h1 class="heading">ORIN VENTURES GROUP</h1>
  <p>Orin Ventures Group Limited is a private property finance company. Orin Ventures Group has capital to directly fund first mortgage, mezzanine and preferred equity financing. We also acquire performing, sub-performing and distressed debt. Orin Ventures' management philosophy emphasises expertise, innovation, wisdom, honesty and competitiveness.</p>
  <div class="btn">READ MORE</div>
</section>

<section class="services">
  <h2 class="heading">OUR SERVICES</h2>
  <div class="service" style="left:134px">
    <div class="service-icon"></div>
    <h3 class="heading">Property Finance</h3>
    <p>Morbi diam mauris viverra in gravida eu mattis in ante Morbi eget arcu Morbi porta libero id ullamcorper nonummy nibh ligula</p>
    <div class="more">READ MORE</div>
  </div>
  <div class="service" style="left:456px">
    <div class="service-icon"></div>
    <h3 class="heading">Debt Funding</h3>
    <p>Morbi diam mauris viverra in gravida eu mattis in ante Morbi eget arcu Morbi porta libero id ullamcorper nonummy nibh ligula</p>
    <div class="more">READ MORE</div>
  </div>
  <div class="service" style="left:778px">
    <div class="service-icon"></div>
    <h3 class="heading">Directly Fund First Mortgage</h3>
    <p>Morbi diam mauris viverra in gravida eu mattis in ante Morbi eget arcu Morbi porta libero id ullamcorper nonummy nibh ligula</p>
    <div class="more">READ MORE</div>
  </div>
</section>

<section class="projects">
  <h2 class="heading">OUR PROJECTS</h2>
  <div class="tile tile-a" role="img" aria-label="Glass office building facade">
    <h3 class="heading">PROJECT TITLE</h3>
    <p>Morbi diam mauris viverra in gravida eu mattis in ante Morbi eget arcu Morb</p>
  </div>
  <div class="tile tile-b" role="img" aria-label="Modern tower seen from below against a pale sky"></div>
  <div class="tile tile-c" role="img" aria-label="Apartment blocks in warm sunlight under a blue sky"></div>
  <div class="btn">VIEW MORE PROJECTS</div>
</section>

<section class="experience">
  <div class="building" role="img" aria-label="Black and white apartment building with balconies"></div>
  <h2 class="heading">PROJECT EXPERIENCE</h2>
  <p>Vivamus porttitor purus nisi eleifend libero a tempus libero lectus feugiat felis Morbi diam mauris viverra in gravida eu mattis in ante Morbi eget arcu Morbi porta libero id ullamcorper nonummy nibh ligula pulvinar metus eget consectetuer augue nisi quis lacus</p>
  <div class="btn">READ MORE</div>
</section>

<section class="contact">
  <div class="contact-item" style="left:156px">
    <svg width="14" height="20" viewBox="0 0 14 20" aria-hidden="true"><path d="M7 0a7 7 0 0 0-7 7c0 5 7 13 7 13s7-8 7-13a7 7 0 0 0-7-7zm0 10a3 3 0 1 1 0-6 3 3 0 0 1 0 6z" fill="#fff"/></svg>
    <span>42 Harlow Lane Suite 7 Austin 78701 TX</span>
  </div>
  <div class="contact-item" style="left:566px">
    <svg width="20" height="20" viewBox="0 0 20 20" aria-hidden="true"><path d="M4 1l3 4-2 2c1 3 4 6 7 7l2-2 4 3-2 3C9 18 2 11 1 3z" fill="none" stroke="#fff" stroke-width="1.4" stroke-linejoin="round"/></svg>
    <span>512.555.0148</span>
  </div>
  <div class="contact-item" style="left:828px">
    <svg width="20" height="15" viewBox="0 0 20 15" aria-hidden="true"><rect x="1" y="1" width="18" height="13" fill="none" stroke="#fff" stroke-width="1.4"/><path d="M1 1l9 7 9-7" fill="none" stroke="#fff" stroke-width="1.4"/></svg>
    <span>info@orinventures.example</span>
  </div>
</section>

<footer class="site-footer">
  <nav class="footer-nav">
    <span>Home</span><span>About</span><span>Team</span><span>Services</span><span>Project Experience</span><span>Contact</span>
  </nav>
  <div class="copyright">© 2017 Company Name &nbsp;All right reserved</div>
  <div class="social" aria-label="Social links"><span></span><span></span><span></span><span></span></div>
</footer>

</body>
</html>
```